Email Banner (QuillStacks)

We require an email banner for our email promotions sent to prospect clients. The banner needs to contain the wording QuillStacks and use the same colour scheme as the logos attached.

This is for B2B professional's so needs to look like a place you would come to read technology articles.

```html
<!DOCTYPE html>
<html lang="en">
<head>
<meta charset="utf-8">
<title>QuillStacks Email Banner</title>
<link rel="stylesheet" href="https://fonts.googleapis.com/css2?family=Source+Sans+3:wght@400;600&display=swap">
<style>
  :root {
    --backdrop: #f8b8a0;
    --brand-red: #d42a34;
    --brand-plum: #951a5c;
    --brand-navy: #233457;
    --plum-dark: #7e1a4a;
    --paper: #f5f5f4;
    --white: #ffffff;
  }
  html, body {
    margin: 0;
    width: 1200px;
    height: 874px;
    overflow: hidden;
    background: var(--backdrop);
    font-family: "Source Sans 3", "Myriad Pro", sans-serif;
  }
  .email-banner {
    position: absolute;
    left: 55px;
    top: 300px;
    width: 1090px;
    height: 251px;
    background: radial-gradient(ellipse at 62% 45%, var(--white) 0%, var(--paper) 70%);
    overflow: hidden;
  }
  .banner-shapes {
    position: absolute;
    inset: 0;
    width: 1090px;
    height: 251px;
  }
  .promo-title {
    position: absolute;
    left: 72px;
    top: 50px;
    width: 250px;
    margin: 0;
    text-align: center;
    color: var(--white);
    font-weight: 400;
    font-size: 27px;
    line-height: 1.2;
  }
  .promo-copy {
    position: absolute;
    left: 76px;
    top: 94px;
    width: 240px;
    margin: 0;
    color: var(--white);
    font-size: 11.6px;
    line-height: 15px;
  }
  .brand-name {
    position: absolute;
    left: 600px;
    top: 62px;
    width: 440px;
    margin: 0;
    text-align: center;
    color: var(--brand-navy);
    font-weight: 600;
    font-size: 76px;
    line-height: 100px;
    letter-spacing: -1px;
  }
</style>
</head>
<body>
  <section class="email-banner" aria-label="QuillStacks email banner">
    <svg class="banner-shapes" viewBox="0 0 1090 251" aria-hidden="true">
      <defs>
        <linearGradient id="panel-gradient" x1="0" y1="0" x2="1" y2="0">
          <stop offset="0" stop-color="var(--brand-red)"/>
          <stop offset="1" stop-color="var(--brand-plum)"/>
        </linearGradient>
        <linearGradient id="stripe-gradient" x1="0" y1="0" x2="1" y2="0">
          <stop offset="0" stop-color="#ffffff" stop-opacity="0.08"/>
          <stop offset="1" stop-color="#e94ba0" stop-opacity="0.45"/>
        </linearGradient>
      </defs>
      <!-- left promo panel -->
      <polygon class="promo-panel" points="0,0 575,0 392,251 0,251" fill="url(#panel-gradient)"/>
      <polygon class="promo-stripe" points="0,18 477,18 463,41 0,41" fill="url(#stripe-gradient)"/>
      <polygon class="promo-stripe-tab" points="471,18 519,18 504,41 457,41" fill="var(--plum-dark)"/>
      <!-- social links -->
      <g class="social-links" fill="none" stroke="var(--white)" stroke-width="2">
        <circle cx="61" cy="197" r="9"/>
        <circle cx="130" cy="197" r="9"/>
        <circle cx="199" cy="197" r="9"/>
        <circle cx="267" cy="197" r="9"/>
        <circle cx="336" cy="197" r="9"/>
      </g>
      <!-- footer accents -->
      <polygon class="accent-navy" points="605,216 645,216 620,251 575,251" fill="var(--brand-navy)"/>
      <polygon class="accent-band" points="655,216 1090,216 1090,251 630,251" fill="url(#panel-gradient)"/>
    </svg>

    <h1 class="promo-title">Lorem ipsum</h1>
    <p class="promo-copy">Lorem ipsum dolor sit amet, consectetuer adipiscing elit, sed diam nonummy nibh euismod tincidunt ut laoreet dolore magna aliquam erat volutpat.</p>

    <p class="brand-name">QuillStacks</p>
  </section>
</body>
</html>
```